Business Card Design Project

Business card design based on the existing logo.

Target Market(s)

Small to medium business owners and CIO's looking for professional IT services.

Industry/Entity Type

Business

Font styles to use
Serif
Sans Serif

Requirements
Must have
• Logo, company name, company details

Text to appear on the business card
Name / Title:
Leon Fairholt
CEO

Address:
Valtiro Limited
Level 3, 42 Kestle St
P O Box 462
Paraparaumu 5391

Other details:
leon@valtiro.co
Ph: 0800 519 308
Mob: +64 21 948 216
www.valtiro.co

Nice to have
• I would look at both single and double sided options. My initial thought is double sided with just the logo with the grey framing for the front and the name and details on the back. But I'm open to other design options.

```html
<!DOCTYPE html>
<html lang="en">
<head>
<meta charset="utf-8">
<title>Valtiro – Business Card</title>
<link rel="stylesheet" href="https://fonts.googleapis.com/css2?family=Arimo:wght@400;700&display=swap">
<style>
  :root {
    --page: #ffffff;
    --frame-grey: #d6d6d8;
    --card-white: #fdfdfd;
    --card-edge: #c9c9cb;
    --brand-blue: #356b8a;
    --ink: #111111;
    --logo-ink: #2a2a2a;
  }
  * { box-sizing: border-box; margin: 0; padding: 0; }
  html, body {
    width: 1200px; height: 900px; overflow: hidden;
    background: var(--page);
    font-family: "Arimo", Arial, sans-serif;
  }
  .sheet { position: relative; width: 1200px; height: 900px; }

  /* Front face */
  .card-front {
    position: absolute; left: 230px; top: 15px;
    width: 739px; height: 435px;
    background: var(--frame-grey);
  }
  .logo-panel {
    position: absolute; left: 282px; top: 51px;
    width: 404px; height: 332px;
    background: #ffffff;
    display: flex; align-items: center; justify-content: center; gap: 16px;
  }
  .logo-mark {
    width: 34px; height: 34px; background: var(--brand-blue);
  }
  .logo-name {
    font-size: 60px; font-weight: 400; color: var(--logo-ink);
    letter-spacing: -0.5px; line-height: 1;
  }

  /* Back face */
  .card-back {
    position: absolute; left: 230px; top: 450px;
    width: 739px; height: 435px;
    background: var(--card-white);
    border: 1.5px solid var(--card-edge);
  }
  .holder { position: absolute; left: 136px; top: 148px; }
  .holder-name {
    font-size: 22px; font-weight: 700; color: var(--brand-blue); line-height: 28px;
  }
  .holder-title {
    font-size: 21px; font-weight: 700; color: var(--ink); line-height: 28px;
  }
  .divider {
    position: absolute; left: 135px; top: 226px;
    width: 470px; height: 2px; background: var(--ink);
  }
  .details {
    position: absolute; top: 252px;
    font-size: 19px; line-height: 25.5px; color: var(--ink);
    list-style: none;
  }
  .details--contact { left: 136px; }
  .details--address { left: 411px; }
</style>
</head>
<body>
<main class="sheet">
  <section class="card-front" aria-label="Card front">
    <div class="logo-panel">
      <span class="logo-mark" aria-hidden="true"></span>
      <span class="logo-name">Valtiro</span>
    </div>
  </section>

  <section class="card-back" aria-label="Card back">
    <div class="holder">
      <p class="holder-name">Leon Fairholt</p>
      <p class="holder-title">CEO</p>
    </div>
    <div class="divider"></div>
    <ul class="details details--contact">
      <li>leon@valtiro.co</li>
      <li>Ph: 0800 519 308</li>
      <li>Mob: +64 21 948 216</li>
      <li>www.valtiro.co</li>
    </ul>
    <ul class="details details--address">
      <li>Valtiro Limited</li>
      <li>Level 3, 42 Kestle St</li>
      <li>P O Box 462</li>
      <li>Paraparaumu 5391</li>
    </ul>
  </section>
</main>
</body>
</html>
```